Postcard flyers for text vouchers

Postcard flyer to drive people to text for local vouchers delivered straight to their mobile, alternatively they can check out the websites.
Double sided, full colour A6 size. 105mm x 148.5mm http://www.brintafold.com/supplying-artwork.html
Postcard will be available in high footfall areas must be eye catching and compelling, but keep message simple. Wording as attached, side one headline grabbing, side two in style of a tag cloud giving a flavour of vouchers/savings available in their local area.
Updates

Project Deadline Extended
Reason: Research has shown wider area for website required therefore by county [Kelmarsh Deals] rather than smaller regions. Focus on entertainment and shopping for flyer.

Target Market(s)

Target 18-55 year olds
Core 25-45???
male and female

Requirements
Must have
• Stand out

```html
<!DOCTYPE html>
<html lang="en">
<head>
<meta charset="utf-8">
<title>Text Vouchers Postcard Flyer</title>
<link rel="stylesheet" href="https://fonts.googleapis.com/css2?family=Black+Ops+One&family=Anton&family=Arimo:wght@700&display=swap">
<style>
  :root {
    --ink: #000000;
    --paper: #ffffff;
    --signal-yellow: #f3e000;
    --voucher-red: #e0323a;
    --frame: #333333;
  }
  * { box-sizing: border-box; margin: 0; padding: 0; }
  html, body { width: 845px; height: 1200px; overflow: hidden; background: var(--paper); }
  body { position: relative; font-family: "Arimo", Arial, sans-serif; color: var(--ink); }

  .side-label {
    position: absolute; left: 53px;
    font: 700 22px "Arimo", Arial, sans-serif;
  }
  .side-label--front { top: 16px; }
  .side-label--back { top: 1152px; }

  .card {
    position: absolute; left: 53px; width: 743px; height: 523px;
    border: 1.5px solid var(--frame); overflow: hidden; background: var(--paper);
  }
  .card--front { top: 73px; }
  .card--back { top: 614px; }

  .card__shapes { position: absolute; inset: 0; }

  /* front */
  .front__chevrons-small { position: absolute; left: 10px; top: 24px; }
  .front__how {
    position: absolute; left: 14px; top: 101px;
    font: 186px/1 "Black Ops One", "Impact", sans-serif;
    letter-spacing: -4px; transform: scaleY(1.42); transform-origin: top left;
    white-space: nowrap;
  }
  .front__much {
    position: absolute; left: 462px; top: 290px;
    font: 26px/1 "Anton", "Impact", sans-serif; letter-spacing: 1px;
    white-space: nowrap;
  }
  .front__save {
    position: absolute; left: 304px; top: 330px;
    font: 120px/1 "Black Ops One", "Impact", sans-serif;
    letter-spacing: -2px; transform: scaleX(0.7); transform-origin: top left;
    white-space: nowrap;
  }

  /* back */
  .back__lead {
    position: absolute; font: 20px/1 "Anton", "Impact", sans-serif;
    letter-spacing: 1px; white-space: nowrap;
  }
  .back__lead--intro { left: 62px; top: 70px; }
  .back__lead--choose { left: 100px; top: 104px; }
  .back__lead--redeem { left: 116px; top: 284px; }
  .back__lead .highlight { color: var(--voucher-red); margin: 0 10px; }
  .area-list { position: absolute; left: 87px; top: 161px; list-style: none; }
  .area-list li { font: 700 18px/32px "Arimo", Arial, sans-serif; }
  .area-list .keyword { color: var(--voucher-red); }

  .back__terms {
    position: absolute; left: 0; right: 0; top: 352px; text-align: center;
    font: 20px/24px "Anton", "Impact", sans-serif; letter-spacing: 1px;
  }
  .back__sites {
    position: absolute; left: 0; right: 0; top: 410px; text-align: center;
    font: 700 17px/22px "Arimo", Arial, sans-serif; color: var(--voucher-red);
  }
  .back__sites .divider { margin: 0 18px; }
</style>
</head>
<body>
  <div class="side-label side-label--front">front</div>

  <section class="card card--front" aria-label="Postcard front">
    <svg class="card__shapes" width="743" height="523" viewBox="0 0 743 523" aria-hidden="true">
      <polygon points="0,132 455,132 710,238 455,337 0,337" fill="var(--signal-yellow)"/>
      <line x1="0" y1="399" x2="296" y2="399" stroke="var(--ink)" stroke-width="1.5" stroke-dasharray="4 3"/>
      <line x1="0" y1="420" x2="743" y2="420" stroke="var(--ink)" stroke-width="1.5"/>
      <line x1="0" y1="443" x2="743" y2="443" stroke="var(--ink)" stroke-width="9" stroke-dasharray="26 14"/>
      <rect x="0" y="481" width="743" height="15" fill="var(--ink)"/>
      <g fill="var(--ink)">
        <polygon points="594,347 648,375 594,403 594,391 626,375 594,359"/>
        <polygon points="666,347 722,375 666,403 666,391 700,375 666,359"/>
      </g>
    </svg>
    <svg class="front__chevrons-small" width="50" height="26" viewBox="0 0 50 26" aria-hidden="true">
      <polygon points="0,2 20,13 0,24 0,19 12,13 0,7" fill="var(--ink)"/>
      <polygon points="26,2 46,13 26,24 26,19 38,13 26,7" fill="var(--ink)"/>
    </svg>
    <h1 class="front__how">HOW</h1>
    <p class="front__much">MUCH CAN YOU</p>
    <p class="front__save">SAVE?</p>
  </section>

  <section class="card card--back" aria-label="Postcard back">
    <svg class="card__shapes" width="743" height="523" viewBox="0 0 743 523" aria-hidden="true">
      <polygon points="551,106 743,106 743,311 630,311 417,212" fill="var(--signal-yellow)"/>
      <rect x="0" y="478" width="743" height="18" fill="var(--ink)"/>
    </svg>
    <p class="back__lead back__lead--intro">YOUR LOCAL MONEY SAVING <span class="highlight">VOUCHERS</span> ARE WAITING FOR YOU</p>
    <p class="back__lead back__lead--choose">SIMPLY CHOOSE YOUR AREA AND TEXT AS FOLLOWS:</p>
    <ul class="area-list">
      <li>For savings in Malvern text voucher <span class="keyword">m</span> to 64321</li>
      <li>For savings in Worcester text voucher <span class="keyword">w</span> to 64321</li>
      <li>For savings in Hereford text voucher <span class="keyword">h</span> to 64321</li>
    </ul>
    <p class="back__lead back__lead--redeem">TO REDEEM SIMPLY QUOTE THE VOUCHER CODE OR PRINT OFF. EASY!</p>
    <p class="back__terms">STANDARD TEXT RATES APPLY. NO SPAM POLICY. UNSUBSCRIBE AT ANY TIME.<br>SEE YOUR VOUCHER WEBSITES FOR EVEN MORE SAVINGS</p>
    <p class="back__sites">www.malverntextdeals.co.uk<span class="divider">|</span>www.worcestertextdeals.co.uk<br>www.herefordtextdeals.co.uk</p>
  </section>

  <div class="side-label side-label--back">back</div>
</body>
</html>
```